Voltwise - Flyer design

Description -
Motorhome and Caravan EWOFs
Recreational Vehicles (such as caravans, motorhomes, RVs, Boats etc) and Relocatable buildings that can be connected to an electricity supply must be regularly checked for electrical safety. An EWOF needs to be issued every 4 years.
Pre-purchase house inspections
A pre-purchase electrical inspection prior to buying a home can be used to identify any dangerous and unsafe electrical parts of the installation that may be costly to repair once the property has been purchased. Giving you peace of mind when buying your new home.
High risk Electrical inspections
All Prescribed Electrical Work that falls under the High Risk category must be inspected by a Registered Electrical Inspector and have a Record of Inspection certificate issued.
Electric Vehicle Chargers
Any electrical vehicle charger that can be accessed by the public (ie in a non-domestic situation) must be periodically inspected and certified every 12 months.
General Electrical Services
Domestic and commercial - We do new builds, Renovations, Maintenance and more!
Dean Porter - Electrician and Electrical Inspector
Ph - 0275381942
Dean@voltwise-sample.co.nz
Auckland
------
I also want there to be a few symbols similar to the files I have attached.
The main areas that I am hoping to find work is with caravans/motohomes and EV car chargers so these symbols are quite important.
Thanks so much

```html
<!DOCTYPE html>
<html lang="en">
<head>
<meta charset="utf-8">
<title>Voltwise – Motorhome and Caravan EWOFs</title>
<link href="https://fonts.googleapis.com/css2?family=Montserrat:wght@600;700&family=Roboto:wght@400;500&display=swap" rel="stylesheet">
<style>
  :root {
    --green: #76bc43;
    --ink: #1e1e1e;
    --text: #2a2a2a;
    --white: #ffffff;
    --card: #f3f3f3;
    --card-line: #d9d9d9;
  }
  * { box-sizing: border-box; margin: 0; padding: 0; }
  html, body { width: 849px; height: 1200px; overflow: hidden; background: var(--white); }
  .flyer { position: relative; width: 849px; height: 1200px; background: var(--white); font-family: "Roboto", Arial, sans-serif; color: var(--text); }
  .bands { position: absolute; left: 0; top: 0; }
  .brand { position: absolute; top: 58px; left: 0; width: 849px; display: flex; justify-content: center; align-items: center; gap: 14px; }
  .brand-mark { width: 30px; height: 30px; background: var(--green); }
  .brand-name { font-family: "Montserrat", Arial, sans-serif; font-weight: 700; font-size: 52px; color: var(--ink); letter-spacing: 0.5px; }
  .hero-title { position: absolute; top: 228px; left: 0; width: 849px; text-align: center; font-family: "Montserrat", Arial, sans-serif; font-weight: 700; font-size: 37px; line-height: 38px; color: var(--white); }
  .hero-rule { position: absolute; top: 319px; left: 392px; width: 64px; height: 3px; background: var(--green); }
  .hero-text { position: absolute; top: 333px; left: 40px; width: 769px; text-align: center; font-size: 17.5px; line-height: 22px; color: var(--white); }
  .card { position: absolute; background: var(--card); border: 1.5px solid var(--card-line); text-align: center; padding: 0 16px; }
  .card-icon { display: block; width: 72px; height: 60px; margin: 0 auto; background: var(--green); }
  .card-title { font-family: "Montserrat", Arial, sans-serif; font-weight: 700; font-size: 20px; line-height: 22px; color: var(--ink); margin-top: 14px; }
  .card-text { font-size: 15.6px; line-height: 20.6px; color: var(--text); margin-top: 6px; }
  .card-text strong { font-weight: 500; color: var(--ink); }
  .card-a { left: 72px; top: 541px; width: 344px; height: 288px; }
  .card-b { left: 433px; top: 541px; width: 344px; height: 288px; }
  .card-c { left: 72px; top: 846px; width: 344px; height: 228px; }
  .card-d { left: 433px; top: 846px; width: 344px; height: 228px; }
  .seal { position: absolute; left: 387px; top: 801px; }
  .footer { position: absolute; left: 0; top: 1120px; width: 849px; height: 80px; background: var(--ink); }
  .name-tag { position: absolute; z-index: 2; left: 154px; top: 1087px; width: 263px; height: 41px; background: var(--green); color: var(--white); font-family: "Montserrat", Arial, sans-serif; font-weight: 700; font-size: 27px; line-height: 41px; text-align: center; }
  .role-tag { position: absolute; z-index: 1; left: 406px; top: 1096px; width: 290px; height: 23px; background: var(--green); color: var(--white); font-size: 15px; line-height: 23px; padding-left: 18px; }
  .contacts { position: absolute; left: 0; top: 1146px; width: 849px; display: flex; justify-content: center; gap: 22px; color: var(--white); font-size: 17px; line-height: 32px; }
  .contact { display: flex; align-items: center; gap: 4px; }
  .contact svg { width: 32px; height: 32px; }
</style>
</head>
<body>
<div class="flyer">
  <svg class="bands" width="849" height="560" viewBox="0 0 849 560" aria-hidden="true">
    <path d="M0 102 Q424 230 849 139 L849 493 Q424 420 0 493 Z" fill="var(--ink)"/>
    <path d="M0 120 Q200 170 356 187 Q180 160 0 128 Z" fill="var(--white)"/>
    <path d="M81 478 Q500 400 849 480 L849 537 Q520 430 81 478 Z" fill="var(--green)"/>
  </svg>

  <div class="brand">
    <span class="brand-mark"></span>
    <span class="brand-name">Voltwise</span>
  </div>

  <h1 class="hero-title">MOTORHOME AND<br>CARAVAN EWOFS</h1>
  <div class="hero-rule"></div>
  <p class="hero-text">Recreational Vehicles (such as caravans, motorhomes, RVs, Boats etc) and<br>Relocatable buildings that can be connected to an electricity supply must be regularly<br>checked for electrical safety. An EWOF needs to be issued every 4 years.</p>

  <section class="card card-a">
    <svg class="card-icon" viewBox="0 0 72 60" role="img" aria-label="House inspection icon">
      <rect width="72" height="60" fill="var(--green)"/>
      <g fill="none" stroke="var(--ink)" stroke-width="3" stroke-linejoin="round" stroke-linecap="round">
        <path d="M16 30 L32 16 L48 30"/>
        <path d="M21 26 L21 44 L35 44"/>
        <circle cx="45" cy="38" r="7"/>
        <path d="M50 43 L57 50"/>
      </g>
    </svg>
    <h2 class="card-title">PRE-PURCHASE HOUSE<br>INSPECTIONS</h2>
    <p class="card-text">A pre-purchase electrical inspection prior<br>to buying a home can be used to identify<br>any dangerous and unsafe electrical<br>parts of the installation that may be<br>costly to repair once the property has<br>been purchased. Giving you peace of<br>mind when buying your new home.</p>
  </section>

  <section class="card card-b">
    <svg class="card-icon" viewBox="0 0 72 60" role="img" aria-label="High risk electrical icon">
      <rect width="72" height="60" fill="var(--green)"/>
      <path d="M36 12 L52 18 L52 31 Q52 42 36 49 Q20 42 20 31 L20 18 Z" fill="none" stroke="var(--ink)" stroke-width="3" stroke-linejoin="round"/>
      <path d="M39 19 L30 33 L36 33 L33 42 L43 27 L37 27 Z" fill="var(--ink)"/>
    </svg>
    <h2 class="card-title">HIGH RISK ELECTRICAL<br>INSPECTIONS</h2>
    <p class="card-text">All Prescribed Electrical Work that<br>falls under the High Risk category<br>must be inspected by a Registered<br>Electrical Inspector and have a Record<br>of Inspection certificate issued.</p>
  </section>

  <section class="card card-c">
    <svg class="card-icon" viewBox="0 0 72 60" role="img" aria-label="Electric vehicle charger icon">
      <rect width="72" height="60" fill="var(--green)"/>
      <path d="M47 19 A15 15 0 1 0 47 41" fill="none" stroke="var(--ink)" stroke-width="3" stroke-linecap="round"/>
      <rect x="44" y="23" width="10" height="14" rx="2" fill="var(--ink)"/>
      <path d="M54 26 L59 26 M54 34 L59 34" stroke="var(--ink)" stroke-width="3" stroke-linecap="round"/>
      <path d="M36 20 L28 31 L34 31 L31 40 L40 28 L34 28 Z" fill="var(--ink)"/>
    </svg>
    <h2 class="card-title">ELECTRIC VEHICLE<br>CHARGERS</h2>
    <p class="card-text">Any electrical vehicle charger that can be<br>accessed by the public (ie in a non-do-<br>mestic situation) must be periodically<br>inspected and certified every 12 months.</p>
  </section>

  <section class="card card-d">
    <svg class="card-icon" viewBox="0 0 72 60" role="img" aria-label="Electrical tools icon">
      <rect width="72" height="60" fill="var(--green)"/>
      <path d="M26 14 Q18 16 20 24 L22 26 L22 46" fill="none" stroke="var(--ink)" stroke-width="4" stroke-linecap="round"/>
      <path d="M46 14 Q54 16 52 24 L50 26 L50 46" fill="none" stroke="var(--ink)" stroke-width="4" stroke-linecap="round"/>
      <path d="M39 16 L30 31 L36 31 L33 44 L43 27 L37 27 Z" fill="var(--ink)"/>
    </svg>
    <h2 class="card-title">GENERAL ELECTRICAL<br>SERVICES</h2>
    <p class="card-text"><strong>Domestic and commercial</strong> - We do<br>new builds, Renovations, Mainte-<br>nance and more!</p>
  </section>

  <svg class="seal" width="74" height="74" viewBox="0 0 74 74" aria-hidden="true">
    <polygon points="22,2 52,2 72,22 72,52 52,72 22,72 2,52 2,22" fill="var(--green)" stroke="var(--white)" stroke-width="3"/>
    <path d="M23 38 L33 47 L52 26" fill="none" stroke="var(--ink)" stroke-width="5" stroke-linecap="round" stroke-linejoin="round"/>
  </svg>

  <div class="footer"></div>
  <div class="name-tag">DEAN PORTER</div>
  <div class="role-tag">Electrician and Electrical Inspector</div>

  <div class="contacts">
    <span class="contact">
      <svg viewBox="0 0 32 32" aria-hidden="true"><circle cx="16" cy="16" r="15" fill="var(--green)"/><path d="M11 8 L14 8 L15.5 12.5 L13.5 14 Q15 18 18 19 L19.5 17 L24 18.5 L24 21.5 Q23 24 20 24 Q9 22 8 11 Q8 8 11 8 Z" fill="var(--ink)"/></svg>
      0275381942
    </span>
    <span class="contact">
      <svg viewBox="0 0 32 32" aria-hidden="true"><circle cx="16" cy="16" r="15" fill="var(--green)"/><rect x="8" y="10.5" width="16" height="11" rx="1.5" fill="none" stroke="var(--ink)" stroke-width="2"/><path d="M8.5 11.5 L16 17 L23.5 11.5" fill="none" stroke="var(--ink)" stroke-width="2"/></svg>
      Dean@voltwise-sample.co.nz
    </span>
  </div>
</div>
</body>
</html>
```